Book cover design for a collection of poetry - The Lanternfield

Book cover and back design need to be moody, nostalgic, reflective, ethereal. Melancholy and other worldly. Cover design should not be time specific to a period or place but if applicable should reflect British landscape. Book cover should be in tones of blue and must include the title and author (THE LANTERNFIELD BY CORWIN BLACKETT). We love the idea of rain, and looking out of a window. See attached designs. A world you are observing but not in.

Industry/Entity Type

Book Publisher

Font styles to use
Serif
Script

Colors
3176b5
3377b5
85acd3
eaf1f7
0792cd
33a6d7
86cae7
ecf7fb
86cfc6

Requirements
Must have
• The colour blue in it, must be melancholy and reflective.
Nice to have
• Rain in the cover.
Should not have
• Any bright colours.

```html
<!DOCTYPE html>
<html lang="en">
<head>
<meta charset="utf-8">
<title>The Lanternfield — Cover Spread</title>
<link rel="stylesheet" href="https://fonts.googleapis.com/css2?family=Cinzel:wght@500;600&family=Cormorant+Garamond:wght@500;600&family=Tinos:wght@700&display=swap">
<style>
  :root {
    --page-bg: #ffffff;
    --navy-deep: #14203f;
    --navy: #1f3161;
    --blue-mid: #3176b5;
    --blue-soft: #85acd3;
    --sky-pale: #eaf1f7;
    --dusk-gold: #e9dc8a;
    --sill: #2a3766;
    --spine-band: rgba(26, 40, 84, 0.82);
    --title-silver: #dfe9f4;
    --title-edge: #0e1730;
    --author-cream: #f6f1cf;
    --blurb-white: #ffffff;
  }
  * { margin: 0; padding: 0; box-sizing: border-box; }
  html, body {
    width: 1200px; height: 602px; overflow: hidden;
    background: var(--page-bg);
  }
  .spread {
    position: absolute; left: 206px; top: 21px;
    width: 787px; height: 560px; overflow: hidden;
  }
  .back-scene {
    position: absolute; left: 0; top: 0; width: 376px; height: 560px;
    background:
      linear-gradient(90deg, var(--navy-deep) 0%, var(--navy) 38%, rgba(31,49,97,0) 52%),
      linear-gradient(180deg, #8aa2cf 0%, #6f8cc4 35%, #c9cdb8 62%, #4d67a8 74%, var(--sill) 86%, #b7a6b8 100%);
  }
  .front-scene {
    position: absolute; left: 376px; top: 0; width: 411px; height: 560px;
    background:
      radial-gradient(ellipse 60% 18% at 35% 78%, rgba(233,220,138,0.85), rgba(233,220,138,0) 70%),
      linear-gradient(180deg, #c7d3ea 0%, var(--blue-soft) 25%, #7f97cf 45%, #e8e0b8 58%, #4f72c0 68%, #c9c7a8 74%, #3c5aa6 82%, var(--sill) 88%, #b9a8bf 100%);
  }
  .spine {
    position: absolute; left: 376px; top: 0; width: 34px; height: 560px;
    background: var(--spine-band);
  }
  .spine-text {
    position: absolute; left: 17px;
    writing-mode: vertical-rl;
    transform: translateX(-50%);
    font-family: "Tinos", "Times New Roman", serif;
    color: var(--blurb-white);
    font-size: 15px; letter-spacing: 0.5px; white-space: nowrap;
  }
  .spine-title { top: 54px; text-transform: uppercase; }
  .spine-author { top: 402px; font-size: 16px; }
  .blurb {
    position: absolute; left: 76px; top: 112px; width: 222px;
    font-family: "Tinos", "Times New Roman", serif; font-weight: 700;
    font-size: 10.6px; line-height: 14.7px; text-align: center;
    color: var(--blurb-white);
    text-shadow: 0 0 3px rgba(20,32,63,0.5);
  }
  .blurb p + p { margin-top: 14.7px; }
  .front-title {
    position: absolute; left: 410px; top: 48px; width: 377px;
    text-align: center;
    font-family: "Cinzel", "Times New Roman", serif; font-weight: 600;
    color: var(--title-silver);
    text-shadow: -1px -1px 0 var(--title-edge), 1px 1px 0 var(--title-edge),
                 2px 2px 3px rgba(14,23,48,0.7);
    line-height: 1;
  }
  .front-title .title-the { display: block; font-size: 40px; margin-left: 20px; }
  .front-title .title-main { display: block; font-size: 34px; margin-top: 10px; letter-spacing: 0.5px; }
  .front-author {
    position: absolute; left: 410px; top: 490px; width: 377px;
    text-align: center;
    font-family: "Cormorant Garamond", "Times New Roman", serif; font-weight: 600;
    font-size: 29px; color: var(--author-cream);
    text-shadow: 0 0 4px #0e1730, 1px 1px 2px #0e1730;
  }
</style>
</head>
<body>
  <main class="spread">
    <div class="back-scene" role="img" aria-label="Photograph of a rain-streaked window in a dim room, dusk sky in blues and pale gold beyond"></div>
    <div class="front-scene" role="img" aria-label="Photograph of raindrops on a window pane, bare tree silhouetted against a blue and golden dusk sky"></div>

    <section class="back-cover">
      <div class="blurb">
        <p>The lanternfield is a collection of poetry. Told in two parts we first meet Charles- aged, crippled and left alone in his inherited marsh house- reflecting on his life and his marriage to beautiful Alice who we meet in part two. Alice is suicidal, manically depressed and struggling with life as a wife and mother. She meets, harbors and falls in love with a soldier during WWII and her world is changed forever.</p>
        <p>Moving through the 20th Century, this life and the next, the lanternfield interweaves grief, loss, the after-life, mental illness, and ultimately the true nature of love.</p>
      </div>
    </section>

    <aside class="spine">
      <span class="spine-text spine-title">The Lanternfield</span>
      <span class="spine-text spine-author">Corwin Blackett</span>
    </aside>

    <section class="front-cover">
      <h1 class="front-title">
        <span class="title-the">The</span>
        <span class="title-main">Lanternfield</span>
      </h1>
      <p class="front-author">Corwin Blackett</p>
    </section>
  </main>
</body>
</html>
```